Glow of Gold Needs a Facebook Design

We need a Facebook Design for a new company based in Atlanta, GA called "Glow Of Gold".
We custom design:
• Figure Suits
• Physique Suits
• Bikini Suits
• Posing Trunks
• Physique Shorts and Boardshorts

We would like to see designs that match the colors of our logo. The final design should be Modern, Serious, and Elegant.

Target Market(s)

Fitness Industry
Figure, Physique, Bikini, Bodybuilding Competitiors

Industry/Entity Type

Fitness

Requirements
Must have
• The page must be Modern, Serious, and Elegant.
Nice to have
• The colors and design coordinate with the Logo.

```html
<!DOCTYPE html>
<html lang="en">
<head>
<meta charset="utf-8">
<title>Glow Of Gold – Facebook Cover</title>
<link rel="stylesheet" href="https://fonts.googleapis.com/css2?family=Bebas+Neue&display=swap">
<style>
  :root {
    --backdrop: #808080;
    --band-white: #ffffff;
    --deep-red: #7a0a0c;
    --mid-red: #c0161b;
    --hot-red: #e23a2a;
    --flare: #f39a4a;
    --ink-light: #ffffff;
    --brand-red: #a3141a;
  }
  html, body {
    margin: 0;
    padding: 0;
    width: 1200px;
    height: 1000px;
    overflow: hidden;
    background: var(--backdrop);
  }
  .canvas {
    position: relative;
    width: 1200px;
    height: 1000px;
  }
  .cover {
    position: absolute;
    left: 313px;
    top: 394px;
    width: 576px;
    height: 213px;
    overflow: hidden;
    background:
      linear-gradient(115deg, rgba(0,0,0,0.85) 0%, rgba(0,0,0,0) 14%),
      linear-gradient(120deg, var(--deep-red) 0%, var(--mid-red) 35%, var(--hot-red) 65%, var(--flare) 100%);
  }
  .brand-band {
    position: absolute;
    left: 0;
    top: 0;
    width: 340px;
    height: 57px;
    background: linear-gradient(90deg, var(--band-white) 0%, var(--band-white) 60%, rgba(255,255,255,0) 100%);
  }
  .brand-name {
    position: absolute;
    left: 14px;
    top: 13px;
    margin: 0;
    font-family: "Bebas Neue", sans-serif;
    font-weight: 400;
    font-size: 32px;
    line-height: 1;
    letter-spacing: 1px;
    color: var(--brand-red);
  }
  .services {
    position: absolute;
    left: 133px;
    top: 77px;
    font-family: "Bebas Neue", sans-serif;
    color: var(--ink-light);
  }
  .services-heading {
    margin: 0 0 2px;
    font-size: 17px;
    font-weight: 400;
    line-height: 18px;
  }
  .services-list {
    margin: 0;
    padding: 0 0 0 17px;
    list-style: disc;
    font-size: 16px;
    line-height: 18.7px;
  }
  .athletes-photo {
    position: absolute;
    right: 0;
    top: 0;
    width: 262px;
    height: 213px;
    background: linear-gradient(90deg, rgba(176,90,60,0) 0%, #b0603f 22%, #c98662 50%, #b86a48 78%, #d85a38 100%);
  }
</style>
</head>
<body>
  <main class="canvas">
    <section class="cover">
      <div class="brand-band">
        <p class="brand-name">Glow Of Gold</p>
      </div>
      <div class="services">
        <p class="services-heading">We custom design:</p>
        <ul class="services-list">
          <li>Figure suits</li>
          <li>Physique suits</li>
          <li>Bikini suits</li>
          <li>Posing trunks</li>
          <li>Physique shorts and boardshorts</li>
        </ul>
      </div>
      <div class="athletes-photo" role="img" aria-label="Photo of three competitors posing in custom sequined bikini suits"></div>
    </section>
  </main>
</body>
</html>
```